Wholistic Health Clinic (Chiropractic Osteopathic Naturapathic Homeopathic New Website Design

Create a beautiful website for Fenwick Chiropractic clinic that has been in the Sutherland Shire for over 40 years, that exemplifies the passion for helping people with their health goals using that may include a variety of techniques including Chiropractic, Osteopathy, Acupuncture, Applied Kinesiology, Retained Neonatal Reflexes, Nutritional Advice, Exercise Prescription, Decompression therapy, Massage and Stress management techniques.
We have a wholistic approach that includes Nutritional, Emotional and Physical health

(A more detailed draft will be supplied shortly)

Pages:
Home page
About Us Page
Team Page
Contact page
Terms of service Page
Privacy Page
and any other relevant page(s)

Will supply photos for:
- The Team Page and their qualifications & brief resume
- About Us page

Will supply logos for:
BPN
TORVEX
PLORIVEN
GRANTLEAF
MVA
KPO

Target Market(s)

main target Parents of young children and those 20's to 60's who live in the Sutherland Shire & have disposable income (that said almost everybody would benefit from their services)

Coding

Coded - Design and coding required

Number of Pages Required

5+ page

Font styles to use
Sans Serif

Requirements
Must have
• Please follow the brief

1. Easy to manage ourselves to add alerts (like Covid 19 compliance & Harbel week etc.) & update content like photos of team members etc.
2. Must be responsive and look good on mobile devices
3. must be fast loading
4. Logo on every page
5. Easy navigation on every page
6. Phone number must be clickable
7. Terms of service & Privacy pages
8. Slider on page 1 using photo of healthy people of all ages enjoying various lifestyles & ability to add other photos easily
Should not have
• no testimonials or any non compliant elements according to the BPN

```html
<!DOCTYPE html>
<html lang="en">
<head>
<meta charset="utf-8">
<title>Fenwick Chiropractic – Wholistic Health Clinic</title>
<link href="https://fonts.googleapis.com/css2?family=Rajdhani:wght@500;600;700&family=Lato:wght@400;700;900&display=swap" rel="stylesheet">
<style>
:root{
  --navy:#1b3f7f;
  --blue:#1f56a8;
  --ink:#222;
  --muted:#555;
  --grey-band:#dfe3e9;
  --footer:#2a2a2a;
  --alert:#e6e7e9;
  --white:#fff;
}
*{box-sizing:border-box;margin:0;padding:0}
html,body{width:1200px;height:3807px;overflow:hidden;background:var(--white)}
body{font-family:'Lato',sans-serif;color:var(--ink);position:relative}
.abs{position:absolute}

/* hero */
.hero{position:absolute;left:0;top:0;width:1200px;height:717px;
  background:linear-gradient(180deg,#d9a55e 0%,#f0b94f 28%,#e59a3a 45%,#b56524 62%,#4a2412 85%,#1d0e08 100%)}
.brand{position:absolute;left:90px;top:16px;width:230px;text-align:center}
.brand-dot{width:52px;height:52px;border-radius:50%;background:var(--navy);margin:0 auto 10px;display:block}
.brand-name{display:block;font-weight:900;font-size:16px;letter-spacing:1px;color:var(--navy);text-transform:uppercase;line-height:18px}
.brand-tag{display:block;font-size:8.5px;font-weight:700;color:var(--navy);letter-spacing:.5px;margin-top:2px}
.nav{position:absolute;top:64px;left:0;font-family:'Rajdhani',sans-serif;font-weight:600;font-size:15px;color:#111}
.nav a{position:absolute;white-space:nowrap;color:#111;text-decoration:none}
.nav a.active{color:var(--blue)}
.social-top{position:absolute;top:21px;display:flex;gap:12px;left:996px}
.social-top span{width:20px;height:20px;border-radius:50%;background:#7a6a55;display:block}
.phone-top{position:absolute;left:928px;top:61px;font-size:15px;color:#111;display:flex;align-items:center;gap:6px}
.tagline{position:absolute;left:81px;top:312px;font-family:'Rajdhani',sans-serif;font-weight:600;font-size:46px;color:#1a1209;letter-spacing:-.5px}
.thumb{position:absolute;top:616px;width:143px;height:80px;border:3px solid #fff}
.arrow{position:absolute;top:640px}

/* intro cards */
.card{position:absolute;top:794px;width:305px;height:414px;background:#fff;border-radius:8px;box-shadow:0 3px 14px rgba(0,0,0,.12);text-align:center;overflow:hidden}
.card-img{height:177px;width:100%}
.card h3{font-family:'Rajdhani',sans-serif;font-weight:700;font-size:22px;margin-top:36px;color:#111}
.card p{font-size:15px;line-height:18.5px;color:var(--muted);padding:0 24px;margin-top:8px}
.more{font-size:12px;font-weight:700;color:var(--blue);display:inline-block}
.more::after{content:" ›"}
.btn{display:inline-block;background:var(--navy);color:#fff;font-size:12px;font-weight:700;padding:8px 18px;border-radius:16px}
.btn::after{content:" ›"}

/* about */
.about{position:absolute;left:0;top:1293px;width:1200px;height:651px;background:var(--grey-band)}
.about h2{position:absolute;left:55px;top:56px;font-family:'Rajdhani',sans-serif;font-weight:700;font-size:38px;color:#111}
.svc{position:absolute;background:#fff;border-radius:4px;box-shadow:0 2px 6px rgba(0,0,0,.15);height:95px}
.svc h4{position:absolute;left:12px;top:14px;font-family:'Rajdhani',sans-serif;font-weight:600;font-size:16px;line-height:18px;color:#111}
.svc p{position:absolute;left:12px;font-size:12px;line-height:15px;color:#333}
.svc .pic{position:absolute;right:6px;top:6px;width:78px;height:83px}
.svc.accent h4,.svc.accent p{color:var(--blue)}
.diagram{position:absolute;left:739px;top:1405px;width:388px;height:400px;background:linear-gradient(180deg,#f4f5f7,#e9ebee);border-radius:4px}

/* team */
.team-title{position:absolute;left:0;width:1200px;top:2022px;text-align:center;font-family:'Rajdhani',sans-serif;font-weight:700;font-size:30px;color:#111}
.team-rule{position:absolute;top:2080px;left:473px;width:266px;height:1px;background:#888}
.team-rule::after{content:"";position:absolute;left:127px;top:-5px;width:11px;height:11px;border-radius:50%;background:#333}
.member{position:absolute;top:2148px;width:300px;text-align:center}
.avatar{width:162px;height:162px;border-radius:50%;margin:0 auto}
.member h4{font-family:'Rajdhani',sans-serif;font-weight:700;font-size:19px;line-height:25px;margin-top:22px;color:#222}
.member .role{color:var(--blue);font-size:13px;margin-top:6px}
.member p{font-size:14px;line-height:18px;color:#555;margin-top:14px;padding:0 22px}
.member .more{margin-top:16px}

/* wellness */
.wellness{position:absolute;left:0;top:2609px;width:1200px;height:588px;background:linear-gradient(180deg,#6c86b9,#5570a8 60%,#4f69a1)}
.pillar{position:absolute;top:84px;width:340px;text-align:center;color:#fff}
.ring{width:260px;height:260px;margin:0 auto;border-radius:50%;border:2px dashed rgba(255,255,255,.9);display:flex;align-items:center;justify-content:center}
.ring div{width:230px;height:230px;border-radius:50%}
.pillar h3{font-weight:900;font-size:20px;margin-top:42px;letter-spacing:.5px}
.pillar p{font-size:15px;line-height:20px;margin-top:10px;padding:0 50px}

/* partners */
.partner{position:absolute;top:3277px;width:190px;height:91px;border:1px solid #cfcfcf;background:#fff;display:flex;align-items:center;justify-content:center}
.partner span{display:block;width:120px;height:34px;border-radius:4px;background:#9aa3ad}

/* alert */
.alert{position:absolute;left:0;top:3436px;width:1200px;height:67px;background:var(--alert);text-align:center;line-height:67px;font-size:17px;color:#222}

/* footer */
.footer{position:absolute;left:0;top:3503px;width:1200px;height:304px;background:var(--footer);color:#fff}
.f-brand{position:absolute;left:89px;top:75px;width:230px;text-align:center}
.f-brand .dot{width:54px;height:54px;border-radius:50%;background:#fff;margin:0 auto 12px}
.f-brand .name{font-weight:900;font-size:17px;letter-spacing:1px;text-transform:uppercase;color:#fff;border-top:2px solid var(--blue);padding-top:8px}
.f-brand .tag{font-size:9px;font-weight:700;letter-spacing:.5px;margin-top:2px}
.f-social{position:absolute;top:190px;left:123px;display:flex;gap:28px}
.f-social span{width:20px;height:20px;border-radius:50%;background:#fff;display:block}
.f-col h5{position:absolute;top:56px;font-variant:small-caps;font-size:22px;letter-spacing:2px;font-weight:400;text-transform:lowercase}
.f-col h5::first-letter{text-transform:uppercase}
.f-item{position:absolute;font-size:13px;line-height:17px;color:#eee}
.f-item svg{position:absolute;left:-20px;top:2px}
.copy{position:absolute;top:266px;font-size:12.5px;color:#eee}
</style>
</head>
<body>

<!-- HERO -->
<section class="hero" role="img" aria-label="Sunset over hills with a woman raising her arms in joy"></section>
<div class="brand">
  <span class="brand-dot"></span>
  <span class="brand-name">Fenwick Chiropractic</span>
  <span class="brand-tag">WHOLISTIC HEALTH CLINIC</span>
</div>
<nav class="nav">
  <a class="active" style="left:468px">HOME</a>
  <a style="left:551px">ABOUT US</a>
  <a style="left:661px">TEAM</a>
  <a style="left:742px">CONTACT US</a>
</nav>
<div class="social-top"><span></span><span></span><span></span></div>
<div class="phone-top">
  <svg width="15" height="15" viewBox="0 0 24 24"><path fill="#111" d="M6.6 10.8a15.1 15.1 0 0 0 6.6 6.6l2.2-2.2a1 1 0 0 1 1-.25 11.4 11.4 0 0 0 3.6.57 1 1 0 0 1 1 1V20a1 1 0 0 1-1 1A17 17 0 0 1 3 4a1 1 0 0 1 1-1h3.5a1 1 0 0 1 1 1c0 1.25.2 2.45.57 3.57a1 1 0 0 1-.25 1z"/></svg>
  + (1800) 555 0143
</div>
<h1 class="tagline">be active, be strong, be better</h1>

<div class="thumb" style="left:78px;background:linear-gradient(135deg,#e9eef2,#b9c7d2)" role="img" aria-label="Practitioner examining a patient"></div>
<div class="thumb" style="left:259px;background:linear-gradient(180deg,#f3c76a,#6b4a22)" role="img" aria-label="Group of friends jumping at sunset"></div>
<div class="thumb" style="left:437px;background:linear-gradient(135deg,#f2eee9,#d7b7a7)" role="img" aria-label="Person holding a sore neck"></div>
<div class="thumb" style="left:619px;background:linear-gradient(135deg,#e8e8e6,#bfc2c6)" role="img" aria-label="Senior woman receiving care"></div>
<div class="thumb" style="left:798px;background:linear-gradient(135deg,#efe7e3,#c9b1a6)" role="img" aria-label="Back massage treatment"></div>
<div class="thumb" style="left:977px;background:linear-gradient(180deg,#9fd0e3,#e3b8b6)" role="img" aria-label="Woman with lower back pain at the beach"></div>
<svg class="arrow" style="left:30px" width="16" height="26" viewBox="0 0 16 26"><path d="M13 2 3 13l10 11" fill="none" stroke="#fff" stroke-width="3"/></svg>
<svg class="arrow" style="left:1144px" width="16" height="26" viewBox="0 0 16 26"><path d="M3 2l10 11L3 24" fill="none" stroke="#fff" stroke-width="3"/></svg>

<!-- INTRO CARDS -->
<article class="card" style="left:92px">
  <div class="card-img" style="background:linear-gradient(135deg,#c9d7e3,#6c8fb0)" role="img" aria-label="Chiropractor adjusting a patient's back"></div>
  <h3>WHO WE ARE</h3>
  <p>Fenwick Chiropractic, situated in Carrowdale and established for over 40 years, is passionate about helping you achieve your health care goals. We use a unique approach...</p>
  <a class="more" style="margin-top:20px">Find out More</a>
</article>
<article class="card" style="left:449px">
  <div class="card-img" style="background:linear-gradient(135deg,#e6e4e0,#a9a29a)" role="img" aria-label="Chiropractor explaining a spine model to a patient"></div>
  <h3>WHAT WE DO</h3>
  <p style="margin-top:18px">We use many Chiropractic techniques in our clinic to help patients manage a range of musculoskeletal conditions and these are modified to all ages...</p>
  <a class="btn" style="margin-top:18px">Find out More</a>
</article>
<article class="card" style="left:810px">
  <div class="card-img" style="background:linear-gradient(135deg,#dfe6ee,#8fa6bf)" role="img" aria-label="Practitioner reviewing results with a patient"></div>
  <h3>WHAT TO EXPECT</h3>
  <p>If you've never had Chiropractic before, don't worry. We will explain everything as we go and answer any of your questions as you have them.</p>
  <a class="more" style="margin-top:20px">Find out More</a>
</article>

<!-- ABOUT -->
<section class="about">
  <h2>About Us</h2>
</section>
<div class="svc" style="left:55px;top:1432px;width:283px">
  <h4>Chiropractic</h4><p style="top:40px">All bodily function is controlled<br>by the brain through...</p>
  <div class="pic" style="background:linear-gradient(180deg,#2a5fb4,#0d2f6b)" role="img" aria-label="Illustrated spine highlighted in glowing blue"></div>
</div>
<div class="svc accent" style="left:55px;top:1552px;width:283px">
  <h4>Applied Kinesiology</h4><p style="top:40px">A tool used only by health<br>care practitioners registered...</p>
  <div class="pic" style="background:#f1f1f1" role="img" aria-label="Small triangle health diagram"></div>
</div>
<div class="svc" style="left:55px;top:1673px;width:283px">
  <h4>Retained Neonatal Reflexes</h4><p style="top:40px">A reflex is an action that occurs<br>without us having ...</p>
  <div class="pic" style="background:linear-gradient(135deg,#dfe8f0,#c9a98a)" role="img" aria-label="Baby sitting beside a teddy bear"></div>
</div>
<div class="svc" style="left:55px;top:1794px;width:283px;height:98px">
  <h4>Chiropractic Care During<br>Pregnancy</h4><p style="top:58px">Using modified pregnancy<br>specific techniques...</p>
  <div class="pic" style="background:linear-gradient(135deg,#d9ecee,#9ec7c8)" role="img" aria-label="Pregnant woman holding her belly"></div>
</div>
<div class="svc" style="left:375px;top:1487px;width:277px;height:93px">
  <h4>Chiropractic For<br>Babies &amp; Children</h4><p style="top:54px">Using modified pregnancy<br>specific techniques...</p>
  <div class="pic" style="background:linear-gradient(135deg,#e8e6e3,#b1aaa3)" role="img" aria-label="Practitioner gently treating a baby"></div>
</div>
<div class="svc" style="left:375px;top:1608px;width:277px;height:93px">
  <h4>Sports Chiropractic</h4><p style="top:40px">The focus of sports chiropra-<br>ctic is to provide care...</p>
  <div class="pic" style="background:linear-gradient(135deg,#a56b48,#3a2a22)" role="img" aria-label="Runner's legs on a track"></div>
</div>
<div class="svc" style="left:375px;top:1729px;width:277px;height:96px">
  <h4>Acupuncture &amp; Dry Needling</h4><p style="top:40px">Acupuncture is based on the<br>4000yr old...</p>
  <div class="pic" style="background:linear-gradient(135deg,#eef2f6,#e4b9a8)" role="img" aria-label="Acupuncture needles in skin"></div>
</div>

<div class="diagram" role="img" aria-label="Triangle of health diagram: anatomical figure inside a circle and triangle, labelled N, AMC, NL, CSF, NV, chemical, mental and structure"></div>

<!-- TEAM -->
<h2 class="team-title">OUR TEAM</h2>
<div class="team-rule"></div>
<div class="member" style="left:104px">
  <div class="avatar" style="background:linear-gradient(135deg,#f0e6e0,#c98e6e)" role="img" aria-label="Portrait of Dr Owen Talbrook"></div>
  <h4>DR OWEN TALBROOK<br>DC., DO.</h4>
  <div class="role">(CHIROPRACTOR, OSTEOPATH)</div>
  <p>GWP (Owen) Talbrook DC., DO.. is one of the nation's leading authorities on Wholistic Health Care.</p>
  <a class="more">Find out More</a>
</div>
<div class="member" style="left:460px">
  <div class="avatar" style="background:linear-gradient(135deg,#efe9e2,#b8926f)" role="img" aria-label="Portrait of Dr Mara Ellison"></div>
  <h4>DR MARA ELLISON<br>B.SC., M. CHIRO.</h4>
  <div class="role">(CHIROPRACTOR)</div>
  <p>GWP (Owen) Talbrook DC., DO.. is one of the nation's leading authorities on Wholistic Health Care.</p>
  <a class="more">Find out More</a>
</div>
<div class="member" style="left:793px">
  <div class="avatar" style="background:linear-gradient(135deg,#ecebea,#8f7562)" role="img" aria-label="Portrait of Dr Nina Castell"></div>
  <h4>DR NINA CASTELL<br>B.SC. M. CHIRO.</h4>
  <div class="role">(CHIROPRACTOR)</div>
  <p>GWP (Owen) Talbrook DC., DO.. is one of the nation's leading authorities on Wholistic Health Care.</p>
  <a class="more">Find out More</a>
</div>

<!-- WELLNESS -->
<section class="wellness" role="img" aria-label="Faded background of a practitioner with a patient">
  <div class="pillar" style="left:63px">
    <div class="ring"><div style="background:radial-gradient(circle,#d9843c,#6a7a3a 55%,#4a4a4a)" role="img" aria-label="Heart-shaped bowl of fresh vegetables and fruit"></div></div>
    <h3>NUTRITION</h3>
    <p>At Fenwick Chiropractic we place great importance on the correct foods and nutritional supplements for optimal health &amp; wellbeing...</p>
  </div>
  <div class="pillar" style="left:431px">
    <div class="ring"><div style="background:radial-gradient(circle,#f1c2a0,#8ea9d6 70%)" role="img" aria-label="Fingers with drawn expressions showing emotions"></div></div>
    <h3>EMOTIONS</h3>
    <p>The way you think affects the chemical and physical health of your body. We have various stress management techniques...</p>
  </div>
  <div class="pillar" style="left:777px">
    <div class="ring"><div style="background:radial-gradient(circle,#c9a07e,#6d5b52 70%)" role="img" aria-label="People working out in a gym"></div></div>
    <h3>EXERCISE</h3>
    <p>How you move your body greatly affects its function, either positively or negatively. We can help you rehabilitate following injury...</p>
  </div>
</section>

<!-- PARTNERS -->
<div class="partner" style="left:77px"><span></span></div>
<div class="partner" style="left:291px"><span style="background:#2b6fb7"></span></div>
<div class="partner" style="left:505px"><span></span></div>
<div class="partner" style="left:720px"><span style="background:#7d7d7d"></span></div>
<div class="partner" style="left:931px"><span style="background:#3b3b3b"></span></div>

<!-- ALERT -->
<div class="alert">ALERT: currently responding to <b>COVID-19</b>, Harbel health week, promotions</div>

<!-- FOOTER -->
<footer class="footer">
  <div class="f-brand">
    <div class="dot"></div>
    <div class="name">Fenwick Chiropractic</div>
    <div class="tag">WHOLISTIC HEALTH CLINIC</div>
  </div>
  <div class="f-social"><span></span><span></span><span></span><span></span></div>

  <div class="f-col">
    <h5 style="left:352px">Contact Us</h5>
    <div class="f-item" style="left:381px;top:109px">
      <svg width="10" height="13" viewBox="0 0 10 14"><path fill="#fff" d="M5 0a5 5 0 0 0-5 5c0 4 5 9 5 9s5-5 5-9a5 5 0 0 0-5-5zm0 7a2 2 0 1 1 0-4 2 2 0 0 1 0 4z"/></svg>
      Harlow Street 5248,<br>Kestrel Bay</div>
    <div class="f-item" style="left:381px;top:158px">
      <svg width="12" height="12" viewBox="0 0 24 24"><path fill="#fff" d="M6.6 10.8a15.1 15.1 0 0 0 6.6 6.6l2.2-2.2a1 1 0 0 1 1-.25 11.4 11.4 0 0 0 3.6.57 1 1 0 0 1 1 1V20a1 1 0 0 1-1 1A17 17 0 0 1 3 4a1 1 0 0 1 1-1h3.5a1 1 0 0 1 1 1c0 1.25.2 2.45.57 3.57a1 1 0 0 1-.25 1z"/></svg>
      02 5550 1926 , 0400 555 318</div>
    <div class="f-item" style="left:381px;top:189px">
      <svg width="12" height="11" viewBox="0 0 12 11"><rect x=".5" y=".5" width="11" height="10" fill="none" stroke="#fff"/><path d="M1 4h10" stroke="#fff"/></svg>
      www.fenwickchiro.example</div>
    <div class="f-item" style="left:381px;top:221px">
      <svg width="12" height="9" viewBox="0 0 12 9"><rect width="12" height="9" fill="#fff"/><path d="M0 0l6 5 6-5" fill="none" stroke="#2a2a2a"/></svg>
      support@fenwickchiro.example</div>
  </div>

  <div class="f-col">
    <h5 style="left:644px">Quick Links</h5>
    <div class="f-item" style="left:644px;top:108px">HOME</div>
    <div class="f-item" style="left:644px;top:137px">ABOUT US</div>
    <div class="f-item" style="left:644px;top:167px">TEAM</div>
    <div class="f-item" style="left:644px;top:195px">CONTACT</div>
  </div>

  <div class="f-col">
    <h5 style="left:870px">Clinic Hours</h5>
    <div class="f-item" style="left:897px;top:109px;font-size:12px;font-weight:700">
      <svg width="12" height="12" viewBox="0 0 12 12"><circle cx="6" cy="6" r="5.2" fill="none" stroke="#fff"/><path d="M6 3v3h2.5" fill="none" stroke="#fff"/></svg>
      MONDAY TO FRIDAY: 2PM - 6.45PM</div>
    <div class="f-item" style="left:897px;top:134px;font-size:12px;font-weight:700">
      <svg width="12" height="12" viewBox="0 0 12 12"><circle cx="6" cy="6" r="5.2" fill="none" stroke="#fff"/><path d="M6 3v3h2.5" fill="none" stroke="#fff"/></svg>
      SAT: 8AM – 12 NOON</div>
    <div class="f-item" style="left:877px;top:162px;font-size:12px;font-weight:700">CLINIC HOURS MAY VARY,<br>PLEASE CALL US.</div>
    <div class="f-item" style="left:897px;top:208px;font-size:12px;font-weight:700">
      <svg width="12" height="12" viewBox="0 0 24 24"><path fill="#fff" d="M6.6 10.8a15.1 15.1 0 0 0 6.6 6.6l2.2-2.2a1 1 0 0 1 1-.25 11.4 11.4 0 0 0 3.6.57 1 1 0 0 1 1 1V20a1 1 0 0 1-1 1A17 17 0 0 1 3 4a1 1 0 0 1 1-1h3.5a1 1 0 0 1 1 1c0 1.25.2 2.45.57 3.57a1 1 0 0 1-.25 1z"/></svg>
      02 5550 1926 , 0400 555 318</div>
  </div>

  <div class="copy" style="left:136px">Copyright © 2020. Fenwick Chiropractic. All rights reserved</div>
  <div class="copy" style="left:869px">Terms of service &nbsp;&nbsp;&nbsp;&nbsp;|&nbsp;&nbsp;&nbsp;&nbsp;&nbsp; Privacy</div>
</footer>

</body>
</html>
```